Logo & Visitenkarte für Netz-Kompass.de
Zielgruppe
Meine Firma berät zum Thema Aufbau von Onlineshops, wie betreibe ich einen Webshop erfolgreich?
Was ist hierbei zu beachten ? Entwicklung von Konzepten zum Livegang, Entwicklung von Konzepten zur Verbesserung von bereits bestehenden Auftritten.
Zielgruppe: B2B; Firmen, die Beratungsbedarf im Aufbau und in der Führung von Onlineshops haben.
Es richtet sich eher an kleinere und mittlere Firmen in den Bereichen: Einzelhandel, Großhandel, Onlinehandel, Dienstleistungen
Aufgabenstellung
Das Logo soll zum Stil der Seite 'Netz-Kompass.de' (die sich aktuell noch im Aufbau befindet) passen.
Es soll einerseits eine gewisse Seriosität ausstrahlen, andererseits auch eine gewisse Dynamik widerspiegeln, die im ganzen Thema Onlinebusiness drin ist.

```html
<!DOCTYPE html>
<html lang="de">
<head>
<meta charset="utf-8">
<title>Netz-Kompass.de – Visitenkarte</title>
<link rel="stylesheet" href="https://fonts.googleapis.com/css2?family=Fira+Mono:wght@400;500&display=swap">
<style>
  :root {
    --bg: #cacbce;
    --paper: #ffffff;
    --navy: #03376f;
    --sky: #1a8cff;
    --ink: #2b4b7c;
  }
  * { margin: 0; padding: 0; box-sizing: border-box; }
  html, body {
    width: 1200px; height: 1200px; overflow: hidden;
    background: var(--bg);
    font-family: "Fira Mono", monospace;
  }
  .stage {
    position: relative; width: 1200px; height: 1200px;
    display: flex; flex-direction: column; align-items: center; justify-content: center; gap: 60px;
  }
  .card {
    width: 760px; height: 492px;
    background: var(--paper);
    box-shadow: 0 10px 30px rgba(0,0,0,0.12);
  }
  .card-front { padding: 22px; }
  .card-front .panel {
    width: 100%; height: 100%;
    background: var(--navy);
    display: flex; align-items: center; justify-content: center; gap: 30px;
  }
  .logo-mark {
    width: 150px; height: 150px; border-radius: 50%;
    background: var(--sky); flex: none;
  }
  .logo-name {
    color: var(--sky); font-weight: 500; font-size: 50px; line-height: 1.1;
    letter-spacing: 1px;
  }
  .card-back {
    padding: 110px 0 0 150px;
  }
  .person-name {
    color: var(--sky); font-weight: 500; font-size: 38px; letter-spacing: 2px;
    margin-bottom: 24px;
  }
  .contact { list-style: none; color: var(--ink); font-size: 22px; line-height: 1.5; font-weight: 500; }
</style>
</head>
<body>
<main class="stage">
  <section class="card card-front" aria-label="Vorderseite">
    <div class="panel">
      <div class="logo-mark"></div>
      <div class="logo-name">Netz-<br>Kompass.de</div>
    </div>
  </section>
  <section class="card card-back" aria-label="Rückseite">
    <h1 class="person-name">Jorin Talvask</h1>
    <ul class="contact">
      <li>Lindenpfad 7b</li>
      <li>40210 Feldhausen</li>
      <li>T: +49 555 0142</li>
      <li>E: service@netz-kompass.de</li>
      <li>W: www.netz-kompass.de</li>
    </ul>
  </section>
</main>
</body>
</html>
```